Company brochure for our unique consulting business

We are a small consulting business offering a unique set of services to our clients.. In simple terms we are a business improvement consultancy helping our clients get the best out of their businesses. We work with clients across multiple sectors and deliver a variety of services. We want to put together a brochure to cover these main themes:1. Who we are2. What we do3. The type of people we employ4. The sectors we work inWhile the brochure needs to have a certain corporate feel to it, we don't want it to be "boring" or "stiff". We would like it to have a slightly "friendly" or "informal" feel to it, to reflect the type of organisation we are.We have a company website http://tollandvergeadvisory.com , however we do not want to directly replicate the content or feel as we recognise it needs updating.We would like the brochure to be A4 portrait format. We anticipate requiring 12 sides (including covers) but we are happy to be guided on this based on the content we have provided.The attached ppt file gives the detail of the content to be included and also shows the proposed pagination. For the front cover we would like to try 2 versions, one with the TVA logo and one with the Tolland Verge Advisory logo (a file of both is attached)One of the most important pages will be the "Our Services" page. We would like this to cover the centre fold. In the ppt file we have shown an example layout, but this is where we need most help - we are clearly not graphic designers! This page will be the most used page in sales meetings etc.Also attached is the following:1. file for our TollandVerge Advisory company logo.2. File for our TVA company logo3. Files for Derek's signatures (for under photos) - Owen's to follow4. Photo of Derek & Owen (person in purple shirt to be cropped out)Thank you and really excited to see what everyone comes back with.Derek & Owen

Target Market(s)

Very broad - Manufacturing, Healthcare, Hospitality

Industry/Entity Type

Management Consulting

Font styles to use
Other font styles liked:
• We use Swiss721, but happy to be guided by designer

Colors
3276b5
85abd2
0355a3
333333
5c5c5c
9d9d9d
d9d9d9

Requirements
Must have
• Corporate feel
Nice to have
• Slightly friendly feel
• Our standard "blue" is (CORRECTION) - R55 G96 B146 #376092 and our standard grey is R197 G178, B179 - #B3B2B2, which we would like to keep, but other colours we are happy to be guided on. Brand guidelines attached.

```html
<!DOCTYPE html>
<html lang="en">
<head>
<meta charset="utf-8">
<title>Tolland Verge Advisory – Company Brochure</title>
<link rel="stylesheet" href="https://fonts.googleapis.com/css2?family=Arimo:wght@400;700&family=Questrial&display=swap">
<style>
  :root {
    --brand-blue: #3276b5;
    --deep-blue: #0355a3;
    --soft-blue: #85abd2;
    --ink: #333333;
    --ink-mid: #5c5c5c;
    --ink-light: #9d9d9d;
    --rule: #d9d9d9;
    --paper: #ffffff;
    --backdrop: #ebe8e5;
  }
  * { box-sizing: border-box; margin: 0; padding: 0; }
  html, body { width: 1200px; height: 2372px; overflow: hidden; }
  body { background: var(--backdrop); font-family: "Arimo", Arial, sans-serif; color: var(--ink-mid); position: relative; }

  .spread { position: absolute; left: 70px; width: 1060px; height: 750px; display: flex; box-shadow: 0 4px 18px rgba(0,0,0,.12); }
  .spread--cover { top: 31px; }
  .spread--values { top: 811px; }
  .spread--regions { top: 1591px; }
  .page { position: relative; width: 530px; height: 750px; background: var(--paper); overflow: hidden; }
  .page--left { border-right: 1px solid #eeeeee; }

  .heading { font-family: "Questrial", Arial, sans-serif; font-weight: 400; letter-spacing: 1px; text-transform: uppercase; position: absolute; }
  .heading--blue { color: var(--brand-blue); font-size: 40px; }
  .heading--dark { color: var(--ink); font-size: 40px; }
  .body-copy { position: absolute; font-size: 11.5px; line-height: 1.55; color: var(--ink-mid); }
  .body-copy p + p { margin-top: 10px; }

  .photo { position: absolute; }
  .wordmark { position: absolute; display: flex; align-items: center; gap: 8px; color: var(--brand-blue); font-size: 22px; font-weight: 400; }
  .wordmark__square { width: 14px; height: 14px; background: var(--brand-blue); }

  /* Cover */
  .cover-band { position: absolute; left: 0; top: 190px; width: 530px; height: 370px; background: var(--brand-blue); }
  .cover-band--spine { width: 48px; }
  .contact { position: absolute; top: 618px; border-left: 2px solid var(--brand-blue); padding-left: 10px; font-size: 11.5px; line-height: 1.6; color: var(--ink); font-weight: 700; }
  .contact--address { left: 60px; }
  .contact--reach { left: 290px; }
  .cover-rule { position: absolute; left: 72px; top: 100px; width: 2px; height: 470px; background: var(--brand-blue); transform: rotate(-3deg); transform-origin: top; }
  .cover-title { position: absolute; left: 100px; top: 520px; font-weight: 700; font-size: 14px; color: var(--ink); letter-spacing: .5px; }
  .cover-title::after { content: ""; display: block; width: 390px; height: 2px; background: var(--brand-blue); margin-top: 6px; }

  /* Values */
  .values-rule { position: absolute; left: 50px; top: 428px; width: 430px; height: 1px; background: var(--brand-blue); }
  .values-list { position: absolute; left: 50px; top: 448px; width: 430px; list-style: none; border-left: 2px solid var(--brand-blue); }
  .values-list li { position: relative; padding-left: 16px; font-size: 11.5px; line-height: 1.5; margin-bottom: 12px; color: var(--ink-mid); }
  .values-list li::before { content: ""; position: absolute; left: -6px; top: 5px; width: 8px; height: 8px; border-radius: 50%; background: var(--brand-blue); }
  .values-list strong { color: var(--brand-blue); font-weight: 700; }

  /* About */
  .name-tag { position: absolute; background: rgba(255,255,255,.88); border-left: 3px solid var(--brand-blue); padding: 4px 8px; font-size: 12px; font-weight: 700; color: var(--ink); }
  .name-tag span { display: block; font-size: 9.5px; font-weight: 400; color: var(--ink-mid); }

  /* Regions */
  .regions-band { position: absolute; left: 0; top: 0; width: 530px; height: 250px; }
  .map-label { position: absolute; font-size: 10px; color: var(--ink-mid); letter-spacing: .5px; }
</style>
</head>
<body>

<!-- Cover spread -->
<section class="spread spread--cover">
  <div class="page page--left">
    <div class="cover-band"></div>
    <address class="contact contact--address" style="font-style:normal">TVA Limited<br>Harbour Chambers<br>Mill Street, Ashby AB1 2CD</address>
    <address class="contact contact--reach" style="font-style:normal">Tel: +44 (0) 1632 960118<br>enquiries@tollandvergegroup.com<br>www.tollandvergegroup.com</address>
  </div>
  <div class="page page--right">
    <div class="cover-band cover-band--spine"></div>
    <div class="wordmark" style="right:40px; top:36px;"><span>Tolland Verge Advisory</span><span class="wordmark__square"></span></div>
    <div class="cover-rule"></div>
    <div class="photo" role="img" aria-label="Photo of glass city towers under a cloudy sky with an aeroplane overhead" style="left:100px; top:110px; width:390px; height:380px; background:linear-gradient(180deg,#8fa9c4 0%,#c9d6e3 45%,#4d6784 100%);"></div>
    <h2 class="cover-title">MANAGEMENT CONSULTING</h2>
    <div class="body-copy" style="left:100px; top:556px; width:390px;">
      <p>We are a multi-disciplinary Group providing Business Support Services through four focused divisions. Our core offering of Business Improvement, Events Management, Estate Management and Recruitment are integrated with a focus on optimising the People, Process &amp; Assets of the clients we work with.</p>
    </div>
  </div>
</section>

<!-- Values / About spread -->
<section class="spread spread--values">
  <div class="page page--left">
    <div class="photo" role="img" aria-label="Black and white photo of a hand pointing at a sketched diagram, with blue accent bars" style="left:0; top:40px; width:530px; height:300px; background:linear-gradient(135deg,#f2f2f2 0%,#bdbdbd 55%,#6e6e6e 100%);"></div>
    <h2 class="heading heading--blue" style="left:50px; top:375px;">Our Values</h2>
    <div class="values-rule"></div>
    <ul class="values-list">
      <li>Be <strong>TRUSTED</strong> by our team and clients, so that our opinions are sought, and our recommendations acted upon.</li>
      <li>Have a tight but honest relationship with our clients, so that we are seen as a <strong>PARTNER</strong> and not just a supplier.</li>
      <li>Be focused on return on investment, but predominantly always deliver <strong>GREAT VALUE</strong>.</li>
      <li><strong>DEVELOP &amp; INVEST</strong> in our own people to constantly stay one step ahead.</li>
      <li>Work relentlessly to deliver great results for our clients, but ensure we collectively <strong>ENJOY THE JOURNEY</strong>.</li>
      <li>Take <strong>SOCIAL RESPONSIBILITY</strong> seriously by supporting other worthwhile organisations.</li>
    </ul>
  </div>
  <div class="page page--right">
    <h2 class="heading heading--dark" style="left:40px; top:40px;">About Us</h2>
    <div class="body-copy" style="left:40px; top:96px; width:450px;">
      <p>At TVA we constantly strive to deliver the best possible value for our clients. We recognise that it's our clients that define value, not us, so we listen first. Our team brings real expertise, working side by side with your people to help organisations deliver lasting results against their own business plans.</p>
    </div>
    <div class="photo" role="img" aria-label="Black and white photo of the two partners seated at a meeting table" style="left:0; top:190px; width:530px; height:450px; background:linear-gradient(180deg,#e6e6e6 0%,#b4b4b4 50%,#8a8a8a 100%);"></div>
    <div class="name-tag" style="left:110px; top:400px;">Owen Marsh<span>Managing Director</span></div>
    <div class="name-tag" style="left:330px; top:372px;">Derek Halloway<span>Partner Director</span></div>
    <div class="wordmark" style="right:30px; top:600px;"><span class="wordmark__square"></span><span>TVA</span></div>
  </div>
</section>

<!-- Regions / People spread -->
<section class="spread spread--regions">
  <div class="page page--left">
    <svg class="regions-band" viewBox="0 0 530 250" aria-hidden="true">
      <rect width="530" height="250" fill="#3276b5"/>
      <polygon points="0,0 300,0 0,250" fill="#0355a3" opacity=".35"/>
      <polygon points="0,250 530,200 530,250" fill="#ffffff"/>
    </svg>
    <h2 class="heading" style="left:130px; top:140px; color:#fff; font-size:30px;">Our Regions</h2>
    <div class="photo" role="img" aria-label="Blue world map showing the regions served" style="left:50px; top:360px; width:430px; height:210px; border-radius:40px; background:radial-gradient(ellipse at center,#3276b5 0%,#85abd2 70%,#ffffff 100%);"></div>
    <svg style="position:absolute; left:0; top:0;" width="530" height="750" aria-hidden="true">
      <g stroke="#9d9d9d" stroke-width="1">
        <line x1="130" y1="330" x2="130" y2="420"/>
        <line x1="300" y1="330" x2="300" y2="420"/>
        <line x1="110" y1="470" x2="110" y2="600"/>
        <line x1="260" y1="470" x2="260" y2="600"/>
        <line x1="430" y1="470" x2="430" y2="600"/>
      </g>
    </svg>
    <span class="map-label" style="left:90px; top:314px;">NORTH AMERICA</span>
    <span class="map-label" style="left:272px; top:314px;">UK &amp; IRELAND</span>
    <span class="map-label" style="left:88px; top:605px;">EUROPE</span>
    <span class="map-label" style="left:228px; top:605px;">MIDDLE EAST</span>
    <span class="map-label" style="left:416px; top:605px;">APAC</span>
  </div>
  <div class="page page--right">
    <div class="wordmark" style="right:36px; top:34px;"><span class="wordmark__square"></span><span>TVA</span></div>
    <div class="photo" role="img" aria-label="Silhouettes of a team standing before a tall office window, cut into vertical strips" style="left:20px; top:40px; width:420px; height:290px; background:linear-gradient(180deg,#c8d7e8 0%,#6f8fb3 55%,#1f3d63 100%);"></div>
    <h2 class="heading heading--blue" style="left:40px; top:345px;">Our People</h2>
    <div class="body-copy" style="left:40px; top:405px; width:450px;">
      <p>All of our team at TVA started their careers in operational roles. This means we understand what it's like to be in your shoes. Standing shoulder to shoulder with our teams, we have years of experience and we are able to bring the right people to deliver great results, together. Simply put, our team has some of the best people in the industry.</p>
      <p>We also recognise the single person knows everything, so within the team we have experts in their own fields. They are able to bring their specialised skills and expertise, at the right time and in the best way possible.</p>
      <p>Our team also understands the importance of engagement. Everyone in your team will get to know us on first name terms, because we take the time to listen to every one, from shop floor to senior management.</p>
    </div>
  </div>
</section>

</body>
</html>
```